International sports trophy business needs a web design

We need two pages designed for a new company called medalnook. We sell innovative sports trophies via our website and store details of past purchases to allow returning customers to easily place their orders. Customers can log into their accounts using chatterlane or a secondary account login button. The final design should be clean and should focus on the theme of winning the trophy as it is applicable to all sports.

The page should be designed with themes that can be used throughout the site that we'll turn into a cms theme.
Updates

Hi All,

We're half way in to the competition now and I thought it'd be a good time to provide an update on how things are progressing.  First let me thank you for taking part, there's some really great ideas happening here however some of you have requested a mockup for the second page.  I've put that up now and you should be able to find it in the files section of the brief.  Hopefully this will give people a better starting point than before.

To everybody who is still waiting for feedback, be patient, I'm currently working my way through the designs and will be in contact shortly.  I thought in the meantime I could provide a general update as to how I think the competition is progressing and the concepts that I like the most so far. 

For the landing page... The designs that are leading at the moment are not busy or crowded and devote most of the page layout to the front page info-graphic.  The logo, login and primary menu are all easy to identify but not where your eye lands when viewing the page.  The copyright information and secondary menus are there if you look for them.  As far as the style goes we've found that some of the designs feel a little too serious and too adult and we'd like a more playful feel, if you think that your design already is playful, then we probably do too.  Finally I'll add that we like our logo, but that doesn't mean that we want to see it more than once on the landing page (it's pointless and designs that do this will be unlikely to win) and we certainly do not want to see people creating a new logo or changing our name to medalnook.

For the trophy sales page... There are fewer designs done to this specification as some are unwilling to invest the time in design or unwilling to work without a mockup.  The mockup has now been uploaded to the site (we did want to see what kind of ideas would come here if we didn't include one, thanks to those who had a shot).  If you have any other query about the sales page feel free to contact us.

A final general comment, we want to make sure that all of the images used in your designs are not infringing copyright (this includes images in our mockups, we can only guarantee that we own the copyright for the medalnook logo.).

Hi all, the sliders below have been updated to reflect the more playful design feel that we prefer so far.

Target Market(s)

Our target market is sporting and youth focused but must be adult friendly.

Industry/Entity Type

Business

Requirements
Must have
• We want two pages designed, a landing page and a product display page. We would like a common border scheme across both showing the logo (attached) in the top corner, and secondary links along the bottom.

Landing Page - Must Haves

We see trophies as a representation of achievement and something that can be shared with friends and family. We would like to convey this message in a graphic or illustration on the landing page. Currently in the mockup we have a bunch of trophies, this should not be the final image here.

We have attached a wireframe for the basic format that we'd like to see, you're free to expand upon this as you see fit.

Product Display Page - Must Haves

The product display page will feature a coverflow type device that holds images of the available trophies. It should show the category of the trophy, in this case choose a specific sport to feature (up to you). There should be space for the details of the trophy including price, dimensions, product name, product code, material. There should be room on the page for advertising, this will be common throughout the site except for the landing page. You should include buttons to allow you to add the trophy to your shopping cart and a shopping cart graphic somewhere on the page. There should be a menu bar, unique to this page, that allows a user to choose a new trophy to buy, view previous purchases, view current cart and account settings.

Should not have
• The design should be sport neutral, so don't focus on a single sport or category of sports or sports particular to a certain nationality. With that it's probably easier to just focus on the trophy and achievement aspect rather than the sport being played.

```html
<!DOCTYPE html>
<html lang="en">
<head>
<meta charset="utf-8">
<title>Medalnook – Online Trophy Store</title>
<link href="https://fonts.googleapis.com/css2?family=Oswald:wght@400;500;600;700&family=Arimo:wght@400;700&display=swap" rel="stylesheet">
<style>
  :root{
    --crimson:#8c1230;
    --rose:#c0184a;
    --amber:#c8822a;
    --ink:#111111;
    --charcoal:#1b1b1b;
    --panel:#e6e6e6;
    --panel-line:#d2d2d2;
    --page:#ececec;
    --white:#ffffff;
    --link-blue:#1f3fa8;
    --chatter:#3b5a9a;
    --gold:#c99a3e;
  }
  *{box-sizing:border-box;margin:0;padding:0}
  html,body{width:1200px;height:900px;overflow:hidden}
  body{position:relative;background:var(--page);font-family:"Arimo",Arial,sans-serif;color:var(--ink)}
  .abs{position:absolute}

  /* header */
  .site-header{left:0;top:0;width:1200px;height:70px;background:var(--white)}
  .brand{left:130px;top:4px;width:190px;height:62px;display:flex;flex-direction:column;align-items:center}
  .brand-mark{width:40px;height:36px;border-radius:50%;background:var(--crimson)}
  .brand-name{font-size:19px;letter-spacing:3px;color:var(--ink);font-weight:700;margin-top:3px}
  .account{left:830px;top:3px;display:flex;align-items:center;gap:8px;font-size:11px}
  .account .or{border:1px solid #bbb;background:#eee;padding:0 5px;font-size:10px;color:#555}
  .chatter-btn{background:var(--chatter);color:var(--white);font-weight:700;font-size:11px;height:18px;padding:0 8px 0 6px;display:flex;align-items:center;gap:6px;width:190px}
  .chatter-btn .sq{width:13px;height:13px;background:var(--white)}
  .join{right:111px;top:28px;font-size:9px;color:var(--link-blue)}
  .main-nav{left:789px;top:47px;display:flex;gap:2px;list-style:none}
  .main-nav li{width:58px;height:20px;font-size:11px;line-height:20px;text-align:center;background:#e4e4e4;color:var(--crimson)}
  .main-nav li.active{background:var(--crimson);color:var(--white)}
  .rule-top{left:0;top:70px;width:1200px;height:4px;background:var(--crimson)}

  /* hero */
  .hero{left:0;top:76px;width:1200px;height:174px;background:linear-gradient(#f4f4f4,#dcdcdc);border-bottom:2px solid #c9c9c9}
  .hero-line1{left:100px;top:88px;font-family:"Oswald",sans-serif;font-weight:700;font-size:33px;color:var(--amber);letter-spacing:1.6px}
  .hero-line1 b{color:var(--ink);font-weight:700}
  .hero-line2{left:104px;top:137px;font-family:"Oswald",sans-serif;font-weight:600;font-size:23px;color:var(--crimson);letter-spacing:1.9px}
  .hero-web{left:431px;top:174px;width:96px;height:66px;border-radius:50%;background:var(--charcoal);border:3px solid var(--amber);color:var(--white);font-family:"Oswald",sans-serif;font-weight:700;font-size:30px;display:flex;align-items:center;justify-content:center}
  .hero-arrow{left:535px;top:145px}
  .hero-trophies{left:700px;top:100px;width:380px;height:148px;background:radial-gradient(ellipse 190px 80px at 50% 55%,#d6a94c,#b98a3a 55%,rgba(220,220,220,0) 100%)}

  /* sidebar */
  .bar-head{position:relative;height:22px;background:linear-gradient(#3a3a3a,#0d0d0d);color:var(--white);font-family:"Oswald",sans-serif;font-weight:500;font-size:12px;line-height:22px;padding-left:34px;border-radius:3px}
  .bar-head::before{content:"";position:absolute;left:12px;top:7px;width:12px;height:8px;border-radius:50%;background:#ddd}
  .categories{left:121px;top:258px;width:242px}
  .cat-list{list-style:none;margin-top:7px}
  .cat-list li{height:20px;margin-bottom:1.6px;background:var(--panel);border-bottom:1px solid var(--panel-line);font-size:11px;line-height:20px;padding-left:20px;position:relative;letter-spacing:.5px}
  .cat-list li::before{content:"";position:absolute;left:6px;top:6px;border-left:6px solid #999;border-top:4px solid transparent;border-bottom:4px solid transparent}
  .cat-list li.active{color:var(--crimson)}

  /* latest products */
  .latest{left:386px;top:258px;width:693px}
  .slider{left:387px;top:287px;width:692px;height:192px;background:var(--white);border:1px solid #cfcfcf}
  .slide-offer{left:396px;top:293px;width:235px;height:180px;background:linear-gradient(#e9e9e9,#d8d8d8)}
  .slide-title{left:421px;top:296px;font-family:"Oswald",sans-serif;font-weight:500;font-size:28px;color:var(--ink);border-bottom:2px solid var(--ink);line-height:36px}
  .save-badge{left:456px;top:340px;width:110px;height:80px}
  .save-text{left:456px;top:358px;width:110px;text-align:center;color:var(--white);font-size:16px;line-height:20px;letter-spacing:1px}
  .save-text b{color:#ffd24a;font-size:19px;display:block}
  .enjoy{left:396px;top:421px;width:235px;text-align:center;font-size:10px;font-weight:700;color:var(--crimson);letter-spacing:.5px}
  .buy-btn{left:423px;top:440px;width:196px;height:27px;border-radius:14px;background:var(--ink);border-top:3px solid var(--rose);color:var(--white);font-weight:700;font-style:italic;font-size:17px;text-align:center;line-height:24px;letter-spacing:.5px}
  .slide-photo{left:631px;top:293px;width:438px;height:180px;background:radial-gradient(ellipse 260px 140px at 45% 40%,#e0bd62,#a57b2e 45%,#4a3a1c 75%,#1c1c1c)}
  .slide-dots{left:961px;top:457px;display:flex;gap:3px}
  .slide-dots span{width:17px;height:13px;background:#222;color:var(--white);font-size:9px;text-align:center;line-height:13px}
  .slide-dots span.on{background:var(--rose)}

  /* new products */
  .section-title{left:142px;top:495px;width:918px;height:42px;border:1px solid #dedede;background:repeating-linear-gradient(0deg,#f2f2f2 0 2px,#fafafa 2px 4px);text-align:center;font-family:"Oswald",sans-serif;font-weight:600;font-size:14px;letter-spacing:6px;line-height:42px}
  .section-title em{font-style:normal;color:var(--rose)}
  .product{top:551px;width:205px}
  .product-img{width:200px;height:89px;border:1px solid #cfcfcf;background:var(--white);padding:4px}
  .product-img div{width:100%;height:100%;background:radial-gradient(ellipse 40px 38px at 50% 50%,#d4a84a,#b8924a 60%,#dcdcdc 100%)}
  .product h3{font-family:"Oswald",sans-serif;font-weight:600;font-size:16px;color:var(--rose);margin-top:3px;line-height:20px;letter-spacing:-.1px}
  .product p{font-size:10.2px;line-height:9.7px;letter-spacing:.45px;white-space:nowrap}
  .product .more{display:block;width:200px;text-align:right;color:var(--crimson);font-weight:700;font-size:10.5px;margin-top:13px;letter-spacing:.5px}

  /* footer */
  .rule-bottom{left:0;top:786px;width:1200px;height:3px;background:var(--crimson)}
  .site-footer{left:0;top:789px;width:1200px;height:111px;background:var(--charcoal)}
  .foot-col h4{font-family:"Oswald",sans-serif;font-weight:600;font-size:15px;color:var(--amber);line-height:18px}
  .foot-col ul{list-style:none;margin-top:5px}
  .foot-col li{color:var(--white);font-size:10px;line-height:12.2px;padding-left:11px;position:relative;letter-spacing:.8px}
  .foot-col li::before{content:"";position:absolute;left:0;top:2px;border-left:6px solid var(--white);border-top:4px solid transparent;border-bottom:4px solid transparent}
  .foot-col p{color:var(--white);font-size:10px;line-height:9.8px;letter-spacing:.5px;white-space:nowrap;margin-top:1px}
  .social{display:flex;gap:10px;margin-top:8px}
  .social span{display:flex;align-items:center;gap:3px;color:var(--white);font-size:8px}
  .social i{width:14px;height:14px;background:#6b8ac4;display:block}
  .copyright{left:798px;top:882px;font-size:10px;font-weight:700;color:var(--amber);letter-spacing:.3px}
</style>
</head>
<body>

<header class="site-header abs">
  <div class="brand abs"><span class="brand-mark"></span><span class="brand-name">MEDALNOOK</span></div>
  <div class="account abs">
    <span class="login">Login</span><span class="or">or</span>
    <span class="chatter-btn"><span class="sq"></span>Connect with chatterlane</span>
  </div>
  <div class="join abs">not a member yet ? click here to join</div>
  <ul class="main-nav abs">
    <li class="active">Home</li><li>What ?</li><li>Why ?</li><li>Tour</li><li>Help</li>
  </ul>
</header>
<div class="rule-top abs"></div>

<section class="hero abs"></section>
<div class="hero-line1 abs">WELCOME TO <b>MEDALNOOK</b>, THE</div>
<div class="hero-line2 abs">NEWEST ONLINE TROPHY STORE ON THE</div>
<div class="hero-web abs">WEB</div>
<svg class="hero-arrow abs" width="70" height="52" viewBox="0 0 70 52"><path d="M60 4 C48 30 34 38 14 40 L16 32 L2 44 L18 50 L16 44 C40 42 56 30 64 6 Z" fill="#c8822a"/></svg>
<div class="hero-trophies abs" role="img" aria-label="Three gold trophies raised in celebration"></div>

<aside class="categories abs">
  <div class="bar-head">CATEGORIES</div>
  <ul class="cat-list">
    <li class="active">Athelete Trophy</li><li>Basket Ball Trophy</li><li>Cricket Trophy</li>
    <li>Badminton Trophy</li><li>Swimming Trophy</li><li>Motor Sports Trophy</li>
    <li>Hocket Trophy</li><li>Tennis Trophy</li><li>View More Trophy</li>
  </ul>
</aside>

<div class="latest abs"><div class="bar-head">OUR LATEST PRODUCTS</div></div>
<div class="slider abs"></div>
<div class="slide-offer abs"></div>
<div class="slide-title abs">MEDALNOOK</div>
<svg class="save-badge abs" viewBox="0 0 110 80"><polygon fill="#c0184a" points="55,2 62,10 72,5 75,15 86,13 85,24 96,26 91,36 100,42 91,48 96,58 85,60 86,70 75,68 72,78 62,72 55,80 48,72 38,78 35,68 24,70 25,60 14,58 19,48 10,42 19,36 14,26 25,24 24,13 35,15 38,5 48,10"/></svg>
<div class="save-text abs">SAVE<b>20%</b></div>
<div class="enjoy abs">Enjoy Shopping</div>
<div class="buy-btn abs">Buy Now</div>
<div class="slide-photo abs" role="img" aria-label="Hands lifting a large gold cup amid confetti"></div>
<div class="slide-dots abs"><span class="on">1</span><span>2</span><span>3</span><span>4</span><span>5</span></div>

<div class="section-title abs">MEDALNOOK <em>NEW PRODUCTS</em></div>

<article class="product abs" style="left:141px">
  <div class="product-img"><div role="img" aria-label="Gold cup trophy on black base"></div></div>
  <h3>TROPHIES AND SHIELDS</h3>
  <p>Lorem Ipsum is simply dummy text<br>of the printing and typesetting try ne.<br>Lorem Ipsum is simply dummy text<br>of the printing and typesetting restry.<br>Lorem Ipsum is simply,<br>dummy text of the printing and gtting<br>industry.Lorem Ipsum is simply dy<br>text of the printing and typesettingin-<br>dustry.</p>
  <span class="more">more..</span>
</article>
<article class="product abs" style="left:381px">
  <div class="product-img"><div role="img" aria-label="Gold cup trophy with engraved plaque"></div></div>
  <h3>TROPHIES AND SHIELDS</h3>
  <p>Lorem Ipsum is simply dummy text<br>of the printing and typesetting try ne.<br>Lorem Ipsum is simply dummy text<br>of the printing and typesetting restry.<br>Lorem Ipsum is simply,<br>dummy text of the printing and gtting<br>industry.Lorem Ipsum is simply dy<br>text of the printing and typesettingin-<br>dustry.</p>
  <span class="more">more..</span>
</article>
<article class="product abs" style="left:620px">
  <div class="product-img"><div role="img" aria-label="Silver cup trophy on red base"></div></div>
  <h3>TROPHIES AND SHIELDS</h3>
  <p>Lorem Ipsum is simply dummy text<br>of the printing and typesetting try ne.<br>Lorem Ipsum is simply dummy text<br>of the printing and typesetting restry.<br>Lorem Ipsum is simply,<br>dummy text of the printing and gtting<br>industry.Lorem Ipsum is simply dy<br>text of the printing and typesettingin-<br>dustry.</p>
  <span class="more">more..</span>
</article>
<article class="product abs" style="left:860px">
  <div class="product-img"><div role="img" aria-label="Gold, silver and bronze cup trophies"></div></div>
  <h3>TROPHIES AND SHIELDS</h3>
  <p>Lorem Ipsum is simply dummy text<br>of the printing and typesetting try ne.<br>Lorem Ipsum is simply dummy text<br>of the printing and typesetting restry.<br>Lorem Ipsum is simply,<br>dummy text of the printing and gtting<br>industry.Lorem Ipsum is simply dy<br>text of the printing and typesettingin-<br>dustry.</p>
  <span class="more">more..</span>
</article>

<div class="rule-bottom abs"></div>
<footer class="site-footer abs"></footer>
<div class="foot-col abs" style="left:120px;top:795px">
  <h4>COMPANY</h4>
  <ul><li>Home</li><li>About Us</li><li>What ?</li><li>Why ?</li><li>Tour</li><li>Help</li></ul>
</div>
<div class="foot-col abs" style="left:341px;top:795px">
  <h4>MORE INFORMATION</h4>
  <ul><li>Home</li><li>Blog</li><li>News</li><li>New Products</li><li>Clients</li><li>Resources</li></ul>
</div>
<div class="foot-col abs" style="left:632px;top:795px">
  <h4>LATEST NEWS</h4>
  <p>Lorem Ipsum is simply dummy text of the<br>printing and typesetting industry. Lorem Ipsum<br>has been the industry's standard dummy text<br>ever since the 1500s,</p>
</div>
<div class="foot-col abs" style="left:953px;top:795px">
  <h4>CONNECT WITH US</h4>
  <div class="social"><span><i></i>chatterlane</span><span><i></i>Reelyard</span><span><i></i>Chirpwell</span></div>
</div>
<div class="copyright abs">Copyright © 2011 Medalnook. All Rights Reserved</div>

</body>
</html>
```